Brochure Design Project (Design Studio)

Items required:
1-Brochure. We suggest 15Cm X 15 Cm after cutting.
2-Business Card.
3-Head letter.
4-Folder ( folder should carry the Brochure in pocket and the business card in a pocket on the opposite side of the folder.
5-Envelope to carry everything.
This brochure is expected to draw attention of high level management in companies to the quality and creativity of the design work and encourage them to do business with us. note that brochure will be printed in high quality printing and paper.
The game plan is as follows:
Over all description, the theme of the brochure is drawn from the website theme (website will be uploaded shortly, pictures of the website are attached, logo appears in the top left corner). Please avoid direct copying from the website unless it is a creative copying, just draw the theme from there. however, we need it to be elegant, stylish and class in colors and style. This is a MUST.
Furthermore, the main items of the Brochure:
1-The Studio is not just a studio: we will take about how Branding. A file is attached of the content. (slight changes/modification can apply during the designing process)
2-The Process: this one has to be a visual illustration of the process, it has to be very creative, could be elegant arrows and comics, could be elegant drawing, could be an elegant icons. The drawing should be separate from the steps, we need to the drawing and we need to have the steps listed and commentary, or if want to integrate both in one in an artistic way. Just don’t lose track of the theme and elegance. (steps and commentary are attached, slight changes/modification can apply at anytime.
3-Our Team: another drawing of your suggestion to illustrate the team members, we need to include the names and designation as well leave a place for some of them to say what they need to say about their style of designing. I leave it for your imagination to put this all together in a nice attractive visual illustration.
4-Works: this section will generally show the works of our designers. It needs to be focused on the works themselves, client should be able to view the details of the works ( note that when it comes to brochures and websites, we don’t need to reach to the extent with which the client can read the text in those pictures of the website or brochure, but still can see the overall design clearly). Each design is to carry the name of the designer. Last thing, this section will classify works into categories, like, Brochures, Corporate identity, print design. We didn’t finalize those categories, we will provide them to you shortly, last thing to be said, we are planning to include around 25-30 designs of each sub-category, eg. Corporate identity will have 30 business card s designs and 30 stationary designs.
5-Contacts: the company contacts.
We the brochure after printing should be 15x15 Cm.
Creativity and art work is a major player in selection.
general managers, owners
Printing

```html
<!DOCTYPE html>
<html lang="en">
<head>
<meta charset="utf-8">
<title>Velmora Studio — Brochure Cover</title>
<link rel="stylesheet" href="https://fonts.googleapis.com/css2?family=Arimo:wght@400&display=swap">
<style>
  :root {
    --backdrop: #c9c9c9;
    --cover: #030303;
    --brand-grey: #8c8c8c;
    --url-white: #f2f2f2;
    --strip-blue: #5f6f8c;
    --strip-silver: #b9bcc0;
    --strip-amber: #a8623a;
    --strip-rust: #7a2a1c;
  }
  * { margin: 0; padding: 0; box-sizing: border-box; }
  html, body {
    width: 1200px;
    height: 900px;
    overflow: hidden;
    background: var(--backdrop);
  }
  .canvas {
    position: relative;
    width: 1200px;
    height: 900px;
  }
  .brochure-cover {
    position: absolute;
    left: 215px;
    top: 65px;
    width: 790px;
    height: 770px;
    background: var(--cover);
  }
  .colour-strip {
    position: absolute;
    left: 0;
    top: 268px;
    width: 100%;
    height: 22px;
    background: linear-gradient(90deg,
      #2a2f3a 0%,
      var(--strip-blue) 20%,
      #8995a8 38%,
      var(--strip-silver) 55%,
      #9b8a72 66%,
      var(--strip-amber) 80%,
      var(--strip-rust) 100%);
  }
  .brand-name {
    position: absolute;
    left: 0;
    top: 358px;
    width: 100%;
    text-align: center;
    font-family: "Arimo", sans-serif;
    font-weight: 400;
    font-size: 40px;
    letter-spacing: 3px;
    line-height: 48px;
    color: var(--brand-grey);
  }
  .website {
    position: absolute;
    left: 0;
    top: 430px;
    width: 100%;
    text-align: center;
    font-family: "Arimo", sans-serif;
    font-weight: 400;
    font-size: 20px;
    line-height: 26px;
    color: var(--url-white);
  }
</style>
</head>
<body>
  <main class="canvas">
    <section class="brochure-cover">
      <div class="colour-strip" role="img" aria-label="Thin horizontal strip of blurred photographic colour, blue and silver fading to amber and rust"></div>
      <p class="brand-name">Velmora Studio</p>
      <p class="website">www.velmorastudio.com</p>
    </section>
  </main>
</body>
</html>
```